Business Card and Letterhead for new company Vardel GreenWorks, Inc.

Vardel GreenWorks, Inc., an engineering and construction firm that provides services for solid waste landfill gas systems, needs a business card and letterhead. We recently had a logo designed but we are open to some tweaks to logo design and color scheme. Generally, we like "earthy" color tones - greens, browns, oranges. This is a sister company - www.talvoriengineering.example.

Target Market(s)

Solid waste landfill companies - Brindle Disposal, Halcott Hauling, etc.

Industry/Entity Type

Engineering and Construction

Contact Information for Business Card

Name, Title, email, mobile phone, work phone, website. Potential list of services for back of card: LFG Engineering and Design, GCCS Planning and Operational Consulting, Compliance Monitoring and Reporting, Routine Operations & Maintenance, Nonroutine O&M, Construction Management, Construction QA, GCCS Construction

Font styles to use
Sans Serif

Requirements
Must have
• Logo, pertinent information, maybe a tagline (still in development)
Nice to have
• For back of card, considering an engineering scale (attached for another business of ours), but want to look at other options, alternatives. Like the idea of the back of card to have some utility (scale, unit conversion info, list of services) but willing to consider lots of options.
Should not have
• Needs to have a professional (engineering) and technical look, not cartoonish.

```html
<!DOCTYPE html>
<html lang="en">
<head>
<meta charset="utf-8">
<title>Vardel GreenWorks – Business Card</title>
<link rel="stylesheet" href="https://fonts.googleapis.com/css2?family=Fira+Sans:wght@400;500;600&family=Montserrat:wght@400;500&display=swap">
<style>
  :root {
    --backdrop: #9a9a9a;
    --card-white: #ffffff;
    --teal: #2392b0;
    --green: #72b545;
    --orange: #f29420;
    --flame: #f26b22;
    --grey: #808186;
    --ink: #1f1f1f;
    --on-teal: #ffffff;
  }
  * { box-sizing: border-box; margin: 0; padding: 0; }
  html, body { width: 1093px; height: 1200px; overflow: hidden; }
  body {
    position: relative;
    background: var(--backdrop);
    font-family: "Fira Sans", sans-serif;
  }
  .card {
    position: absolute;
    left: 265px;
    width: 580px;
    height: 364px;
    border-radius: 16px;
    overflow: hidden;
    box-shadow: 2px 4px 6px rgba(0,0,0,.35);
  }
  .card--front { top: 225px; background: var(--card-white); }
  .card--back { top: 616px; background: var(--teal); }

  /* Front */
  .wordmark {
    position: absolute;
    font-family: "Fira Sans", sans-serif;
    font-weight: 600;
    white-space: nowrap;
  }
  .card--front .wordmark {
    left: 28px; top: 44px;
    font-size: 27px;
    color: var(--green);
  }
  .brand-accent {
    position: absolute;
    right: -70px; top: 20px;
    width: 320px; height: 320px;
    border-radius: 50%;
    background: var(--teal);
    opacity: .14;
  }
  .person { position: absolute; left: 26px; top: 128px; }
  .person__name { font-size: 22px; font-weight: 400; color: var(--grey); line-height: 1.2; }
  .person__name .first { color: var(--green); }
  .person__name .initial { color: var(--orange); }
  .person__name .cred { color: var(--teal); }
  .person__title { font-size: 13px; color: var(--ink); margin-top: 2px; }
  .address {
    position: absolute; left: 27px; top: 192px;
    font-family: "Montserrat", sans-serif;
    font-size: 13.5px; line-height: 16.5px; color: var(--ink);
  }
  .contact { position: absolute; left: 27px; top: 242px; list-style: none; }
  .contact li {
    display: flex; align-items: center; gap: 9px;
    font-family: "Montserrat", sans-serif;
    font-size: 13px; color: var(--ink);
    height: 19px;
  }
  .contact li + li { margin-top: 8px; }
  .contact li:nth-child(3), .contact li:nth-child(4) { margin-top: 4px; }
  .contact svg { width: 14px; height: 14px; flex: none; fill: var(--green); }

  /* Back */
  .card--back .wordmark {
    left: 36px; top: 166px;
    font-size: 24px;
    color: var(--on-teal);
  }
  .services-rule {
    position: absolute; left: 255px; top: 62px;
    width: 1px; height: 230px; background: var(--on-teal); opacity: .8;
  }
  .services { position: absolute; left: 267px; top: 60px; }
  .services__heading { font-size: 22px; font-weight: 400; color: var(--orange); }
  .services__list { list-style: none; margin-top: 17px; }
  .services__list li {
    display: flex; align-items: center; gap: 8px;
    font-size: 14.5px; color: var(--on-teal); height: 25px;
  }
  .services__list svg { width: 7px; height: 11px; fill: var(--flame); flex: none; }
  .tagline {
    position: absolute; left: 0; right: 0; top: 316px;
    text-align: center;
    font-family: "Montserrat", sans-serif;
    font-size: 13.5px; color: var(--on-teal);
  }
</style>
</head>
<body>

<section class="card card--front" aria-label="Business card front">
  <div class="brand-accent" aria-hidden="true"></div>
  <div class="wordmark">Vardel GreenWorks</div>

  <div class="person">
    <h1 class="person__name"><span class="first">Dorian</span> <span class="initial">K.</span> Ashfeld<span class="cred">, PE</span></h1>
    <p class="person__title">President Principal, Engineer</p>
  </div>

  <p class="address">4410 Ridgecrest Parkway, Ste<br>210 Larkdale, TN 37990</p>

  <ul class="contact">
    <li><svg viewBox="0 0 24 24" aria-hidden="true"><path d="M6.6 10.8a15.2 15.2 0 0 0 6.6 6.6l2.2-2.2c.3-.3.7-.4 1-.2 1.1.4 2.3.6 3.6.6.6 0 1 .4 1 1V20c0 .6-.4 1-1 1A17 17 0 0 1 3 4c0-.6.4-1 1-1h3.5c.6 0 1 .4 1 1 0 1.3.2 2.5.6 3.6.1.3 0 .7-.2 1z"/></svg>888-555-0142</li>
    <li><svg viewBox="0 0 24 24" aria-hidden="true"><path d="M7 1h10a2 2 0 0 1 2 2v18a2 2 0 0 1-2 2H7a2 2 0 0 1-2-2V3a2 2 0 0 1 2-2zm0 3v14h10V4zm5 15.5a1.2 1.2 0 1 0 0 2.4 1.2 1.2 0 0 0 0-2.4z"/></svg>423-555-0187</li>
    <li><svg viewBox="0 0 24 24" aria-hidden="true"><path d="M2 5h20v2l-10 6L2 7zm0 4.3 10 6 10-6V19H2z"/></svg>dashfeld@vardelgreen.example</li>
    <li><svg viewBox="0 0 24 24" aria-hidden="true"><circle cx="12" cy="12" r="10"/></svg>www.vardelgreenworks.example</li>
  </ul>
</section>

<section class="card card--back" aria-label="Business card back">
  <div class="wordmark">Vardel GreenWorks</div>
  <div class="services-rule" aria-hidden="true"></div>
  <div class="services">
    <h2 class="services__heading">List of Services</h2>
    <ul class="services__list">
      <li><svg viewBox="0 0 7 11" aria-hidden="true"><path d="M3.5 0C5 3 7 5 7 7.5a3.5 3.5 0 0 1-7 0C0 5.5 2 4 3.5 0z"/></svg>LFG Engineering and Design</li>
      <li><svg viewBox="0 0 7 11" aria-hidden="true"><path d="M3.5 0C5 3 7 5 7 7.5a3.5 3.5 0 0 1-7 0C0 5.5 2 4 3.5 0z"/></svg>GCCS Planning and Operational Consulting</li>
      <li><svg viewBox="0 0 7 11" aria-hidden="true"><path d="M3.5 0C5 3 7 5 7 7.5a3.5 3.5 0 0 1-7 0C0 5.5 2 4 3.5 0z"/></svg>Compliance Monitoring and Reporting</li>
      <li><svg viewBox="0 0 7 11" aria-hidden="true"><path d="M3.5 0C5 3 7 5 7 7.5a3.5 3.5 0 0 1-7 0C0 5.5 2 4 3.5 0z"/></svg>Compliance Monitoring and Reporting</li>
      <li><svg viewBox="0 0 7 11" aria-hidden="true"><path d="M3.5 0C5 3 7 5 7 7.5a3.5 3.5 0 0 1-7 0C0 5.5 2 4 3.5 0z"/></svg>Nonroutine O&amp;M, Construction Management</li>
      <li><svg viewBox="0 0 7 11" aria-hidden="true"><path d="M3.5 0C5 3 7 5 7 7.5a3.5 3.5 0 0 1-7 0C0 5.5 2 4 3.5 0z"/></svg>Routine Operations &amp; Maintenance</li>
      <li><svg viewBox="0 0 7 11" aria-hidden="true"><path d="M3.5 0C5 3 7 5 7 7.5a3.5 3.5 0 0 1-7 0C0 5.5 2 4 3.5 0z"/></svg>Construction QA</li>
      <li><svg viewBox="0 0 7 11" aria-hidden="true"><path d="M3.5 0C5 3 7 5 7 7.5a3.5 3.5 0 0 1-7 0C0 5.5 2 4 3.5 0z"/></svg>GCCS Construction</li>
    </ul>
  </div>
  <p class="tagline">Still in Development</p>
</section>

</body>
</html>
```